Zelcor Stationary

Design the stationary of Zelcor Promotion Group.

Zelcor is a BTL company, BTL meaning "below the line". In other words Zelcor is a Promotional Marketing company (the company that design the brands promotional activities).

The design should transmit creativity, agility, boldness.

I need:
* Bis Card
* Letter head
* Envelopes, both vertical and horizontal (for legal size), and letter envelope
* Folders
* PPT template (Title page and regular page)
* CD slip (CD envelope)
* ID card (employee card)

And what ever else you want to throw in.
Updates

Guys,

Something I missed from the brief.   The predominat color should be RED.

Also, have fun and play with the exclamation mark (!) of the logo. 

Hi guys, more comments:

Remember that Zelcor is a "creativity" agency, not in the advertising side but on the promotional side, and that should reflect on the stationary.

 I want a bold design.  Bold and yet crisp.

 

Guys, i just uploaded the Logo in AI format.

I Also uploaded the actual Zelcor Bis Card, wich I like.  So I will like to see some designs with that bis card approach.

Guys, I am so sorry, but I notice in your last post that I upladed a wrong design ("13154_marketing_group_zelcor_brief225630.ai").  The problem was that I asked the designer the file in AI format and he send me thw wrong file, and since I dont have Illustrator I could not verify it.

The differences are minor, I just already ask him the correct one (similar to the EPS file).

Sorry                                   

Just post the correct AI file : "Zelcor Logo.ai"

Reason: I'm expecting more designs to choose from and also I wont be available tomorrow to decide.

Reason: Sorry guys, but we are not there yet!

Target Market(s)

Marketing directors, Marketing Managers

Industry/Entity Type

Legal

Requirements
Must have
• Must work with the logo attached.
The predominat color should be RED.
Play and have fun with the exclamation mark (!).
Should not have
• * No old fonts

Should not be:
* boring
* Informal
* rigid

```html
<!DOCTYPE html>
<html lang="en">
<head>
<meta charset="utf-8">
<title>Zelcor Promotion Group – Business Card</title>
<link rel="stylesheet" href="https://fonts.googleapis.com/css2?family=Jost:wght@400;500;700;800&family=Arimo:wght@400;700&display=swap">
<style>
  :root {
    --backdrop: #e9e6e2;
    --brand-red: #a50f22;
    --brand-red-dark: #7e0a18;
    --brand-red-light: #c0172c;
    --card-white: #f6f6f6;
    --card-grey: #e4e4e4;
    --ink: #1c1c1c;
    --ink-soft: #555555;
    --band-dark: #2b2b2b;
    --band-grey: #8a8a8a;
  }
  * { box-sizing: border-box; margin: 0; padding: 0; }
  html, body {
    width: 1200px;
    height: 900px;
    overflow: hidden;
    background: var(--backdrop);
  }
  .canvas {
    position: relative;
    width: 1200px;
    height: 900px;
    display: flex;
    flex-direction: column;
    align-items: center;
    justify-content: center;
    gap: 40px;
  }
  .card {
    position: relative;
    width: 700px;
    height: 400px;
    border-radius: 26px;
    overflow: hidden;
    box-shadow: 0 6px 18px rgba(0,0,0,0.18);
  }

  /* Back of card */
  .card-back {
    background: linear-gradient(120deg, var(--brand-red-light) 0%, var(--brand-red) 45%, var(--brand-red-dark) 100%);
  }
  .card-back .accent-dot {
    position: absolute;
    right: 110px;
    top: 150px;
    width: 120px;
    height: 120px;
    border-radius: 50%;
    background: rgba(255,255,255,0.12);
  }
  .card-back .web-address {
    position: absolute;
    left: 40px;
    bottom: 36px;
    font-family: "Jost", sans-serif;
    font-weight: 400;
    font-size: 22px;
    color: #ffffff;
    letter-spacing: 0.5px;
  }

  /* Front of card */
  .card-front {
    background: linear-gradient(135deg, #ffffff 0%, var(--card-white) 55%, var(--card-grey) 100%);
  }
  .brand {
    position: absolute;
    left: 52px;
    top: 92px;
    display: flex;
    flex-direction: column;
  }
  .brand-row {
    display: flex;
    align-items: center;
    gap: 14px;
  }
  .brand-name {
    font-family: "Jost", sans-serif;
    font-weight: 800;
    font-size: 62px;
    line-height: 1;
    color: var(--ink);
    letter-spacing: -1px;
  }
  .brand-dot {
    width: 18px;
    height: 18px;
    border-radius: 50%;
    background: var(--brand-red);
    margin-top: 18px;
  }
  .brand-tagline {
    font-family: "Jost", sans-serif;
    font-weight: 500;
    font-size: 12.5px;
    letter-spacing: 4.6px;
    color: var(--ink);
    margin-top: 4px;
    text-transform: uppercase;
  }
  .holder {
    position: absolute;
    right: 62px;
    top: 52px;
    text-align: right;
    font-family: "Arimo", sans-serif;
  }
  .holder-name {
    font-weight: 700;
    font-size: 25px;
    color: var(--brand-red);
  }
  .holder-role {
    font-size: 17px;
    color: var(--ink-soft);
    margin-top: 2px;
  }
  .contact {
    position: absolute;
    left: 52px;
    top: 250px;
    font-family: "Jost", sans-serif;
    font-size: 17px;
    line-height: 1.35;
    color: var(--ink);
  }
  .contact .street { font-weight: 500; }
  .contact .label {
    color: var(--brand-red);
    font-weight: 700;
  }
  .card-band {
    position: absolute;
    left: 0;
    bottom: 0;
    width: 700px;
    height: 90px;
  }
</style>
</head>
<body>
<main class="canvas">

  <section class="card card-back" aria-label="Business card back">
    <div class="accent-dot"></div>
    <p class="web-address">www.Zelcor.com</p>
  </section>

  <section class="card card-front" aria-label="Business card front">
    <div class="brand">
      <div class="brand-row">
        <span class="brand-name">zelcor</span>
        <span class="brand-dot"></span>
      </div>
      <span class="brand-tagline">Promotion Group</span>
    </div>

    <div class="holder">
      <p class="holder-name">Your Name</p>
      <p class="holder-role">Position</p>
    </div>

    <div class="contact">
      <p class="street">123, Your Street, Your City, Country, 123.</p>
      <p><span class="label">P</span> (123) 456 7890 <span class="label">F</span> (123) 456 7890</p>
      <p><span class="label">M</span> (123) 456 7890 <span class="label">E</span> info@zelcor.com</p>
    </div>

    <svg class="card-band" viewBox="0 0 700 90" preserveAspectRatio="none" aria-hidden="true">
      <path d="M0 60 C 180 58, 360 48, 520 24 C 600 12, 660 6, 700 4 L700 90 L0 90 Z" fill="var(--brand-red)"/>
      <path d="M0 66 C 200 64, 380 58, 520 42 C 560 38, 590 40, 610 50 C 590 70, 560 90, 540 90 L0 90 Z" fill="var(--band-grey)"/>
      <path d="M0 70 C 200 68, 380 64, 510 52 C 545 50, 570 56, 585 66 C 570 80, 555 90, 540 90 L0 90 Z" fill="var(--band-dark)"/>
    </svg>
  </section>

</main>
</body>
</html>
```